PACKAGING WRAPPER DESIGN For toilet rolls

We are a toilet paper supplier and require a modern looking packaging wrapper for toilet rolls. These are paper wrappers that individually wrap around a toilet roll. Additional need a matching carton as well. Require a modern looking wrapper and carton. This is for a new product line, however if all good would consider a longer term to overhaul existing product line as well.

Colors
0255a3
3276b5
959595
dcdcdc

Requirements
Must have
• Brand Name is Corvin (refer to file attached) must have that brand name.
• This wrapper will be part of our PREMIUM range. So must have
• Corvin Premium Toilet Rolls as the wording. I have attached samples of a toilet wrapper for another line as well as a carton to give you an idea of what I am looking at and the layout etc..

```html
<!DOCTYPE html>
<html lang="en">
<head>
<meta charset="utf-8">
<title>Corvin Premium Toilet Rolls – Wrapper</title>
<link rel="stylesheet" href="https://fonts.googleapis.com/css2?family=Arimo:wght@700&display=swap">
<style>
  :root {
    --brand-blue: #0255a3;
    --mid-blue: #3276b5;
    --edge-blue: #2f86e0;
    --sun-yellow: #f7e21c;
    --warm-yellow: #f3c21a;
    --pale-yellow: #fbf3a8;
    --paper-white: #ffffff;
    --soft-grey: #dcdcdc;
    --stone-grey: #959595;
  }
  * { margin: 0; padding: 0; box-sizing: border-box; }
  html, body {
    width: 1200px;
    height: 1000px;
    overflow: hidden;
    background: var(--paper-white);
  }
  .canvas {
    position: relative;
    width: 1200px;
    height: 1000px;
    background: var(--paper-white);
  }
  .wrapper {
    position: absolute;
    left: 365px;
    top: 250px;
    width: 480px;
    height: 500px;
    background: var(--paper-white);
    overflow: hidden;
    box-shadow: 0 0 0 1px var(--soft-grey);
    font-family: "Arimo", Arial, sans-serif;
    font-weight: 700;
  }
  .edge-band {
    position: absolute;
    left: 0;
    width: 100%;
    height: 12px;
    background: var(--edge-blue);
  }
  .edge-band--top { top: 0; }
  .edge-band--bottom { bottom: 0; }
  .glow-field {
    position: absolute;
    left: 0;
    top: 12px;
    width: 100%;
    height: 340px;
    background:
      radial-gradient(ellipse 60% 45% at 82% 20%, rgba(243,194,26,0.55), rgba(243,194,26,0) 70%),
      radial-gradient(ellipse 55% 40% at 20% 25%, rgba(247,226,28,0.6), rgba(247,226,28,0) 70%),
      linear-gradient(to bottom, var(--sun-yellow) 0%, var(--sun-yellow) 45%, var(--pale-yellow) 78%, var(--paper-white) 100%);
  }
  .brand-name {
    position: absolute;
    left: 0;
    top: 130px;
    width: 100%;
    text-align: center;
    font-size: 104px;
    font-weight: 700;
    line-height: 1;
    color: var(--brand-blue);
  }
  .brand-dot {
    position: absolute;
    left: 228px;
    top: 272px;
    width: 28px;
    height: 28px;
    border-radius: 50%;
    background: var(--brand-blue);
  }
  .range-name {
    position: absolute;
    left: 43px;
    top: 314px;
    width: 100%;
    text-align: center;
    font-size: 36px;
    line-height: 1;
    color: var(--brand-blue);
  }
  .product-type {
    position: absolute;
    left: 272px;
    top: 364px;
    font-size: 13px;
    line-height: 1;
    letter-spacing: 0.5px;
    color: var(--brand-blue);
  }
  .product-spec {
    position: absolute;
    left: 0;
    top: 422px;
    width: 100%;
    text-align: center;
    font-size: 13.5px;
    line-height: 1.35;
    color: var(--edge-blue);
  }
</style>
</head>
<body>
  <main class="canvas">
    <section class="wrapper" aria-label="Corvin Premium Toilet Rolls wrapper">
      <div class="edge-band edge-band--top"></div>
      <div class="glow-field" role="img" aria-label="Warm yellow glowing light backdrop"></div>

      <h1 class="brand-name">Corvin</h1>
      <span class="brand-dot"></span>

      <p class="range-name">Premium</p>
      <p class="product-type">TOILET ROLLS</p>

      <p class="product-spec">400 x 2 Ply Sheets (11cm x 10cm)<br>Re-order Code CP400</p>

      <div class="edge-band edge-band--bottom"></div>
    </section>
  </main>
</body>
</html>
```